Velmira Body Oil Label for 4 -8 oz bottles

We are selling 4 and 8 oz body oils and need a label to put on our bottles. I'm not sure if we want a label for the front and also the back of the bottle or just one label in the front. You can give me examples of each way. Attached is our logo on a blue background but the background will change colors depending on the scent as specified in the design description. Our bottle will be either clear or white with a pump spray type lid as shown in the attached example. Attached are also our design criteria which is needed for the labels.
Updates

We have decided to use the disc top cap and not the pump spray cap. If you are able to, please show us the design on the 4 oz bottle with the disc top cap. Thanks

Target Market(s)

women

Industry/Entity Type

skincare, cosmetics

Font styles to use
Serif
Sans Serif

Requirements
Must have
• stylish name for each scented oil which contrasts the font in the logo. Also must have darker colors since the logo colors are lighter.
Nice to have
• Border around the labels, maybe one solid color or maybe two complimenting colors which go well with the fragrnace name
Should not have
• background colors that match the logo colors

```html
<!DOCTYPE html>
<html lang="en">
<head>
<meta charset="utf-8">
<title>Velmira Body Oils – Cotton Candy Label</title>
<link href="https://fonts.googleapis.com/css2?family=Montserrat:wght@500;600&family=Source+Sans+3:wght@600;700&display=swap" rel="stylesheet">
<style>
  :root {
    --page: #ffffff;
    --teal-light: #5fe0ee;
    --teal: #16bfd5;
    --teal-deep: #0bb2c8;
    --pink: #f2a9da;
    --pink-deep: #e489c4;
    --blush: #f7cbe7;
    --blush-light: #fde6f4;
    --white: #ffffff;
  }
  * { margin: 0; padding: 0; box-sizing: border-box; }
  html, body {
    width: 1200px; height: 1200px; overflow: hidden;
    background: var(--page);
  }
  .canvas {
    width: 1200px; height: 1200px;
    display: flex; align-items: center; justify-content: center;
  }
  .label {
    width: 480px; height: 1080px;
    display: flex; flex-direction: column;
    color: var(--white);
  }
  .label__brand {
    height: 445px;
    background: radial-gradient(ellipse at 40% 40%, var(--teal-light) 0%, var(--teal) 55%, var(--teal-deep) 100%);
    display: flex; align-items: center; justify-content: center;
    gap: 14px;
  }
  .brand__dot {
    width: 22px; height: 22px; border-radius: 50%;
    background: var(--white);
  }
  .brand__name {
    font-family: "Montserrat", sans-serif;
    font-weight: 500;
    font-size: 64px;
    letter-spacing: 1px;
    color: var(--white);
  }
  .label__scent {
    height: 291px;
    background: linear-gradient(90deg, var(--pink) 0%, var(--pink-deep) 100%);
    display: flex; flex-direction: column; align-items: center; justify-content: center;
    font-family: "Montserrat", sans-serif;
    font-weight: 600;
    font-size: 98px;
    line-height: 1.06;
    letter-spacing: -1px;
    padding-top: 10px;
  }
  .label__art {
    height: 202px;
    background: linear-gradient(180deg, var(--blush) 0%, var(--blush-light) 100%);
    display: flex; justify-content: center;
  }
  .art__cotton-candy {
    width: 260px; height: 100%;
    margin-top: -40px;
    border-radius: 120px 120px 40px 40px;
    background: linear-gradient(90deg, #bfe7f0 0%, #9fd8e8 35%, #f4b8cc 60%, #f29bb4 100%);
  }
  .label__footer {
    height: 142px;
    background: linear-gradient(90deg, var(--teal-light) 0%, var(--teal) 100%);
    font-family: "Source Sans 3", sans-serif;
    display: flex; flex-direction: column; align-items: center;
    padding-top: 18px;
  }
  .claims {
    width: 100%;
    display: flex; justify-content: space-between;
    padding: 0 6px;
    font-weight: 600;
    font-size: 19px;
    letter-spacing: -0.3px;
  }
  .net-weight {
    margin-top: 30px;
    font-weight: 700;
    font-size: 33px;
    letter-spacing: -0.3px;
  }
</style>
</head>
<body>
  <main class="canvas">
    <section class="label">
      <header class="label__brand">
        <span class="brand__dot"></span>
        <span class="brand__name">Velmira</span>
      </header>
      <h1 class="label__scent">
        <span>COTTON</span>
        <span>CANDY</span>
      </h1>
      <div class="label__art">
        <div class="art__cotton-candy" role="img" aria-label="Illustration of blue and pink cotton candy on sticks"></div>
      </div>
      <footer class="label__footer">
        <ul class="claims" style="list-style:none">
          <li>NON-GREESY</li>
          <li>WITH VITAMIN E</li>
          <li>ULTRA MOISTURIZING</li>
        </ul>
        <p class="net-weight">Net Wt. 4 fl. oz. (118 mL)</p>
      </footer>
    </section>
  </main>
</body>
</html>
```